Web Design Project

I am looking for a simple website to promote my business called Maltby Fennick Consulting. We provide consulting and implementation services for finance and supply chain processes and systems.

We want to project a professional but innovative image. I have attached a copy of our logo. It is not necessary to stick with the colours in the logo - we encourage you to experiment with the colours and even to change the colours of the logo to fit with your design. Although, on the front page we would like to have the logo with its original colours.

Required sections:
About
What we do
Clients
Contact
Updates

Target Market(s)

Medium to large companies including multi-nationals in all industries.

Industry/Entity Type

Finance

Requirements
Must have
• Required sections:
About
What we do
Clients
Contact

Files

```html
<!DOCTYPE html>
<html lang="en">
<head>
<meta charset="utf-8">
<title>Contact | Maltby Fennick Consulting</title>
<link rel="stylesheet" href="https://fonts.googleapis.com/css2?family=Arimo:wght@400&display=swap">
<style>
  :root {
    --page-bg: #ffffff;
    --brand-navy: #1b5a97;
    --brand-green: #b3d23f;
    --brand-pink: #db7fa3;
    --nav-grey: #7a7a7a;
    --nav-active: #1f1f1f;
    --heading-grey: #666666;
    --body-text: #333333;
    --rule-grey: #e6e6e6;
    --link-blue: #2b6cb0;
  }
  * { margin: 0; padding: 0; box-sizing: border-box; }
  html, body {
    width: 1200px;
    height: 718px;
    overflow: hidden;
    background: var(--page-bg);
  }
  body {
    font-family: "Arimo", Arial, sans-serif;
  }
  .site {
    position: relative;
    width: 1200px;
    height: 718px;
  }
  .brand {
    position: absolute;
    left: 62px;
    top: 92px;
    width: 220px;
    display: flex;
    align-items: center;
    gap: 12px;
    text-decoration: none;
  }
  .brand-dot {
    flex: none;
    width: 30px;
    height: 30px;
    border-radius: 50%;
    background: var(--brand-green);
  }
  .brand-name {
    font-size: 22px;
    line-height: 27px;
    font-weight: 400;
    color: var(--brand-navy);
  }
  .main-nav {
    position: absolute;
    left: 342px;
    top: 162px;
    display: flex;
    list-style: none;
  }
  .main-nav a {
    display: block;
    font-size: 28px;
    line-height: 36px;
    letter-spacing: -1px;
    color: var(--nav-grey);
    text-decoration: none;
  }
  .main-nav li + li { margin-left: 28px; }
  .main-nav .is-current a { color: var(--nav-active); }
  .page-title {
    position: absolute;
    left: 342px;
    top: 287px;
    font-size: 37px;
    line-height: 44px;
    font-weight: 400;
    letter-spacing: -0.5px;
    color: var(--heading-grey);
  }
  .title-rule {
    position: absolute;
    left: 76px;
    top: 348px;
    width: 1090px;
    height: 2px;
    background: var(--rule-grey);
  }
  .accent-bars {
    position: absolute;
    left: 76px;
    top: 346px;
    display: flex;
    gap: 3px;
  }
  .accent-bars span {
    width: 62px;
    height: 6px;
  }
  .accent-bars .bar-navy { background: var(--brand-navy); }
  .accent-bars .bar-green { background: var(--brand-green); }
  .accent-bars .bar-pink { background: var(--brand-pink); }
  .contact-details {
    position: absolute;
    left: 342px;
    top: 376px;
    font-size: 17px;
    line-height: 24px;
    color: var(--body-text);
    font-style: normal;
  }
  .contact-details p + p { margin-top: 30.6px; }
  .contact-details .street-number { color: var(--link-blue); }
</style>
</head>
<body>
  <div class="site">
    <header>
      <a class="brand" href="#">
        <span class="brand-dot" aria-hidden="true"></span>
        <span class="brand-name">Maltby Fennick Consulting</span>
      </a>
      <nav>
        <ul class="main-nav">
          <li><a href="#">about</a></li>
          <li><a href="#">what we do</a></li>
          <li><a href="#">clients</a></li>
          <li class="is-current"><a href="#">contact</a></li>
        </ul>
      </nav>
    </header>

    <main>
      <h1 class="page-title">Contact</h1>
      <div class="title-rule"></div>
      <div class="accent-bars" aria-hidden="true">
        <span class="bar-navy"></span>
        <span class="bar-green"></span>
        <span class="bar-pink"></span>
      </div>
      <address class="contact-details">
        <p>Email us at:</p>
        <p>Phone on:</p>
        <p>Address:</p>
        <p><span class="street-number">1</span> A Street</p>
        <p>A Town</p>
        <p>State</p>
      </address>
    </main>
  </div>
</body>
</html>
```